Cobalt Margin Funds Bus card and Logo

I need a logo design and Bus card design. The fund focuses on evaluating and investing in minerals (sub-surface rights) and real estate.

Cobalt margin refers to a book of knowledge that each plebe gets when entering the Harwick Civic Academy (my alma mater)

Target Market(s)

Investors and financial advisors

Contact Information for Business Card

Simple - perhaps a logo with a theme on book of knowledge

Logo Text

Ex Scientia Imperium

Font styles to use
Serif
Sans Serif

Colors

Designer to choose colors to be used in the design.

Requirements
Must have
• memorable logo that is relatively simple

```html
<!DOCTYPE html>
<html lang="en">
<head>
<meta charset="utf-8">
<title>Cobalt Margin Funds – Business Cards</title>
<link rel="stylesheet" href="https://fonts.googleapis.com/css2?family=Questrial&family=Arimo:wght@400;700&family=Montserrat:wght@700&display=swap">
<style>
  :root {
    --backdrop: #828287;
    --card-light: #ffffff;
    --card-dark: #231f20;
    --ink-grey: #7d7d80;
    --ink-white: #ffffff;
    --accent-blue: #16a6e6;
    --accent-green: #8dc63f;
  }
  * { margin: 0; padding: 0; box-sizing: border-box; }
  html, body {
    width: 1200px; height: 1000px; overflow: hidden;
    background: var(--backdrop);
  }
  .card {
    position: absolute; left: 261px; width: 678px; height: 387px;
  }
  .card--light { top: 85px; background: var(--card-light); color: var(--ink-grey); --accent: var(--accent-blue); }
  .card--dark { top: 528px; background: var(--card-dark); color: var(--ink-white); --accent: var(--accent-green); }

  .brand {
    position: absolute; left: 47px; width: 240px; top: 98px;
    text-align: center;
  }
  .brand__mark {
    display: block; width: 104px; height: 104px; margin: 0 auto 20px;
    border: 8px solid var(--accent); border-radius: 50%;
  }
  .brand__name {
    font-family: "Questrial", sans-serif;
    font-size: 29px; letter-spacing: 1.5px; line-height: 1; white-space: nowrap;
  }
  .brand__sub {
    display: block; font-size: 18px; letter-spacing: 3px; margin-top: 12px;
  }

  .divider {
    position: absolute; left: 310px; top: 67px; width: 2px; height: 253px;
    background: currentColor; opacity: .8;
  }

  .person {
    position: absolute; left: 346px; top: 64px;
    font-family: "Montserrat", sans-serif; font-weight: 700;
    font-size: 24px; letter-spacing: 3px;
  }

  .contact { position: absolute; left: 346px; top: 210px; list-style: none;
    font-family: "Arimo", sans-serif; font-size: 21px; }
  .contact__item { display: flex; align-items: center; height: 40px; }
  .contact__item--phone { font-weight: 700; }
  .contact__icon { width: 22px; height: 22px; margin-right: 10px; fill: currentColor; flex: none; }
  .contact__icon--line { fill: none; stroke: currentColor; stroke-width: 1.6; }
</style>
</head>
<body>

<section class="card card--light">
  <div class="brand">
    <span class="brand__mark"></span>
    <p class="brand__name">COBALT MARGIN <span class="brand__sub">FUNDS</span></p>
  </div>
  <span class="divider"></span>
  <h2 class="person">NAME</h2>
  <ul class="contact">
    <li class="contact__item contact__item--phone">
      <svg class="contact__icon" viewBox="0 0 24 24"><path d="M6.6 10.8a15 15 0 0 0 6.6 6.6l2.2-2.2c.3-.3.7-.4 1-.2 1.1.4 2.3.6 3.6.6.6 0 1 .4 1 1V20c0 .6-.4 1-1 1A17 17 0 0 1 3 4c0-.6.4-1 1-1h3.5c.6 0 1 .4 1 1 0 1.3.2 2.5.6 3.6.1.3 0 .7-.2 1z"/></svg>
      +00 00000000
    </li>
    <li class="contact__item">
      <svg class="contact__icon" viewBox="0 0 24 24"><path d="M1 5h22v14H1zm2 2v.3l9 6 9-6V7z"/></svg>
      cobaltmargin@.....com
    </li>
    <li class="contact__item">
      <svg class="contact__icon contact__icon--line" viewBox="0 0 24 24"><circle cx="12" cy="12" r="10"/><ellipse cx="12" cy="12" rx="4.5" ry="10"/><path d="M2 12h20M4 6.5h16M4 17.5h16"/></svg>
      www.cobaltmargin.com
    </li>
  </ul>
</section>

<section class="card card--dark">
  <div class="brand">
    <span class="brand__mark"></span>
    <p class="brand__name">COBALT MARGIN <span class="brand__sub">FUNDS</span></p>
  </div>
  <span class="divider"></span>
  <h2 class="person">NAME</h2>
  <ul class="contact">
    <li class="contact__item contact__item--phone">
      <svg class="contact__icon" viewBox="0 0 24 24"><path d="M6.6 10.8a15 15 0 0 0 6.6 6.6l2.2-2.2c.3-.3.7-.4 1-.2 1.1.4 2.3.6 3.6.6.6 0 1 .4 1 1V20c0 .6-.4 1-1 1A17 17 0 0 1 3 4c0-.6.4-1 1-1h3.5c.6 0 1 .4 1 1 0 1.3.2 2.5.6 3.6.1.3 0 .7-.2 1z"/></svg>
      +00 00000000
    </li>
    <li class="contact__item">
      <svg class="contact__icon" viewBox="0 0 24 24"><path d="M1 5h22v14H1zm2 2v.3l9 6 9-6V7z"/></svg>
      cobaltmargin@.....com
    </li>
    <li class="contact__item">
      <svg class="contact__icon contact__icon--line" viewBox="0 0 24 24"><circle cx="12" cy="12" r="10"/><ellipse cx="12" cy="12" rx="4.5" ry="10"/><path d="M2 12h20M4 6.5h16M4 17.5h16"/></svg>
      www.cobaltmargin.com
    </li>
  </ul>
</section>

</body>
</html>
```